Cover and back of brochure

Our company sells all kind of filters. Now we are planning to create an image brochure for our company. This brochure should represent our high quality standard, our competence and the trust of the clients in our company.

In the attachment I added covers of other catalogs which we like. Furthermore I added nice pictures in the attachment which were downloaded from glimmerdock. In the first place we downloaded these pictures in a small size, so that several examples can be created. After we decide which picture looks best on the cover, we will buy it in a higher resolution.

More information you find in the added pdf document.

Industry/Entity Type

It Company

Colors

Designer to choose colors to be used in the design.

```html
<!DOCTYPE html>
<html lang="de">
<head>
<meta charset="utf-8">
<title>Filter Brandt – Rückseite Imagebroschüre</title>
<link rel="stylesheet" href="https://fonts.googleapis.com/css2?family=Cabin:wght@500;600&display=swap">
<style>
  :root {
    --sky: #f4f7f2;
    --mist: #cfe0cc;
    --leaf: #8cc63f;
    --valley: #7fb045;
    --ridge: #2f6e45;
    --ridge-dark: #123a26;
    --cloud: #e9ede4;
    --panel: rgba(12, 14, 12, 0.72);
    --text: #ffffff;
  }
  html, body {
    margin: 0;
    padding: 0;
    overflow: hidden;
    background: #ffffff;
  }
  .back-cover {
    position: relative;
    width: 848px;
    height: 1200px;
    overflow: hidden;
    font-family: "Cabin", "Open Sans", sans-serif;
  }
  .landscape {
    position: absolute;
    inset: 0;
    background:
      radial-gradient(ellipse 55% 22% at 35% 4%, rgba(140, 198, 63, 0.55), transparent 70%),
      linear-gradient(180deg,
        var(--sky) 0%,
        var(--mist) 14%,
        #5f9a6a 22%,
        #4f8c52 28%,
        var(--valley) 34%,
        #5fa24a 40%,
        var(--ridge) 44%,
        var(--ridge-dark) 56%,
        #1c4b30 62%,
        var(--cloud) 68%,
        #dfe7d5 72%,
        var(--ridge-dark) 76%,
        #1a4a2e 82%,
        #d9e3cf 90%,
        var(--cloud) 100%);
  }
  .claim {
    position: absolute;
    top: 528px;
    left: 0;
    width: 848px;
    margin: 0;
    text-align: center;
    color: var(--text);
    font-weight: 500;
    font-size: 28px;
    letter-spacing: 0.2px;
  }
  .contact-panel {
    position: absolute;
    left: 0;
    top: 795px;
    width: 456px;
    height: 324px;
    background: var(--panel);
  }
  .contact {
    position: absolute;
    left: 70px;
    top: 64px;
    margin: 0;
    color: var(--text);
    font-size: 17px;
    font-weight: 600;
    line-height: 22px;
    font-style: normal;
  }
  .contact p { margin: 0; }
  .contact .block + .block { margin-top: 22px; }
</style>
</head>
<body>
  <main class="back-cover">
    <div class="landscape" role="img" aria-label="Foto: grüne Blätter über einer nebligen, gestaffelten Berglandschaft mit Wolkenmeer im Tal"></div>

    <h2 class="claim">KOMPETENT. HILFSBEREIT. FREUNDLICH.</h2>

    <section class="contact-panel">
      <address class="contact">
        <div class="block">
          <p>FILTER - BRANDT e.K.</p>
          <p>Inhaber Jonas Weidlich</p>
          <p>Lindenhofer Str. 12</p>
          <p>14482 Havelstadt</p>
        </div>
        <div class="block">
          <p>Tel: 030 / 555 0148</p>
          <p>Fax: 030 / 555 0149</p>
          <p>E-Mail: info@filter-brandt.de</p>
          <p>Web: www.filter-brandt.de</p>
        </div>
      </address>
    </section>
  </main>
</body>
</html>
```